Book cover design about quality management systems

Book cover design that I can display in my website for ore orders
The book is about helping organisations to fully integrate their Quality management systems rather than having a quality system which sits off to the side and adds extra work.
It is aimed at organisations leaders
It is about leaders taking ownership and leading the decision and design of the quality management system and therefore being able to delegate more effectively.

Target Market(s)

CEO of government funded organisations

Industry/Entity Type

Management

Font styles to use
Sans Serif

Colors

Designer to choose colors to be used in the design.

Requirements
Must have
• Ability to be used on website
• Title of the book
• Anchor lantern harvest
• Strap line - Building systems that last
Nice to have
• Not too fussy
• Not a black cover
• Deep Yellow in the design if possible
Should not have
• Anything too feminine

```html
<!DOCTYPE html>
<html lang="en">
<head>
<meta charset="utf-8">
<title>Anchor Lantern Harvest — Book Cover</title>
<link href="https://fonts.googleapis.com/css2?family=Oswald:wght@500&family=Roboto+Condensed:wght@700&display=swap" rel="stylesheet">
<style>
  :root {
    --page-bg: #ffffff;
    --cover-yellow: #fdd52c;
    --cover-yellow-deep: #f9c90f;
    --ink-black: #1d1d1b;
    --ink-red: #e31b23;
    --ink-blue: #1f7fc2;
    --wood: #e6d2ab;
    --wood-shade: #d9c196;
  }
  * { margin: 0; padding: 0; box-sizing: border-box; }
  html, body {
    width: 1200px;
    height: 1200px;
    overflow: hidden;
    background: var(--page-bg);
  }
  .cover {
    position: absolute;
    left: 200px;
    top: 45px;
    width: 800px;
    height: 1110px;
    overflow: hidden;
    background: linear-gradient(90deg, var(--cover-yellow) 0%, var(--cover-yellow-deep) 100%);
  }
  .book-title { font-size: 0; }
  .title-word {
    position: absolute;
    left: 94px;
    width: 612px;
    height: 140px;
    display: flex;
    justify-content: space-between;
    align-items: center;
    font-family: "Oswald", sans-serif;
    font-weight: 500;
    font-size: 168px;
    line-height: 1;
  }
  .title-word span {
    display: block;
    width: 64px;
    text-align: center;
    transform: scaleX(0.72);
  }
  .title-word--first  { top: 78px;  color: var(--ink-black); }
  .title-word--second { top: 424px; color: var(--ink-red); }
  .title-word--third  { top: 772px; color: var(--ink-blue); }

  .label-band {
    position: absolute;
    left: 110px;
    width: 580px;
    height: 48px;
    background: linear-gradient(180deg, var(--wood) 0%, var(--wood-shade) 100%);
    display: flex;
    align-items: center;
    font-family: "Roboto Condensed", sans-serif;
    font-weight: 700;
    color: var(--ink-black);
    text-transform: uppercase;
    white-space: nowrap;
  }
  .label-band--strapline {
    top: 294px;
    padding-left: 44px;
    font-size: 22px;
    letter-spacing: 2.5px;
  }
  .label-band--plain {
    top: 642px;
    transform: rotate(-4.5deg);
    transform-origin: center;
  }
  .label-band--author {
    top: 990px;
    justify-content: center;
    padding-right: 30px;
    font-size: 29px;
    letter-spacing: 3px;
  }
</style>
</head>
<body>
  <main class="cover">
    <h1 class="book-title" aria-label="Anchor Lantern Harvest">
      <div class="title-word title-word--first" aria-hidden="true">
        <span>A</span><span>N</span><span>C</span><span>H</span><span>O</span><span>R</span>
      </div>
      <div class="title-word title-word--second" aria-hidden="true">
        <span>L</span><span>A</span><span>N</span><span>T</span><span>E</span><span>R</span><span>N</span>
      </div>
      <div class="title-word title-word--third" aria-hidden="true">
        <span>H</span><span>A</span><span>R</span><span>V</span><span>E</span><span>S</span><span>T</span>
      </div>
    </h1>

    <p class="label-band label-band--strapline" role="img" aria-label="Wooden pencil carrying the strapline">Building systems that last</p>
    <div class="label-band label-band--plain" role="img" aria-label="Wooden pencil with a red tip, laid at a slight angle"></div>
    <p class="label-band label-band--author" role="img" aria-label="Wooden pencil carrying the author name">Helena Marsh</p>
  </main>
</body>
</html>
```